Brightmoor Crest Real Estate Company needs Website

I need an updated, easy to use website for my Real Estate company based out of Amarillo, TX.
Our current focus is on residential rental properties. However we are looking to expand into multi-family rentals, commercial rentals, and vacation rentals.
We also offer Real Estate Listing services.
The final design should be user friendly.

Target Market(s)

Homeowners and renters

Industry/Entity Type

Real Estate

Coding

Coded - Design and coding required

Number of Pages Required

1 page

Font styles to use
Sans Serif

Requirements
Must have
• Easy to navigate

```html
<!DOCTYPE html>
<html lang="en">
<head>
<meta charset="utf-8">
<title>Brightmoor Crest Properties</title>
<link href="https://fonts.googleapis.com/css2?family=Raleway:wght@500;600;700&family=Open+Sans:wght@400;600;700&display=swap" rel="stylesheet">
<style>
:root{
  --blue:#3d8fd6;
  --band:#6aa3da;
  --ink:#3a3a3a;
  --muted:#666;
  --dark:#2a2a2a;
  --darker:#1e1e1e;
  --field:#222;
  --c-blue:#3b8fd0;--c-red:#c9474f;--c-gold:#e0a81e;--c-teal:#2fa89a;--c-pink:#c8457f;--c-purple:#a066b0;
}
*{box-sizing:border-box;margin:0;padding:0}
html,body{width:1200px;height:2808px;overflow:hidden}
body{font-family:"Open Sans",Arial,sans-serif;color:var(--ink);background:#fff;position:relative}
.wrap{width:1002px;margin:0 auto;position:relative}
h2{font-family:"Raleway",Arial,sans-serif;font-weight:600;font-size:30px;text-align:center;color:#444}
.lead{text-align:center;font-size:13px;color:#555}
/* header */
.site-header{height:90px;display:flex;align-items:center;position:relative}
.brand{position:absolute;left:99px;top:24px;display:flex;align-items:center;gap:10px;font-family:"Raleway",Arial,sans-serif;font-weight:700;font-size:28px;color:#4a4f57}
.brand .dot{width:14px;height:14px;border-radius:50%;background:var(--blue)}
.nav a{position:absolute;top:38px;font-size:12px;color:#333;text-decoration:none}
.nav .caret{font-size:8px;margin-left:6px;color:#777}
.call{position:absolute;left:916px;top:26px;display:flex;align-items:center;gap:12px;font-size:12px;color:#444}
.call .ic{width:38px;height:38px;border-radius:50%;background:var(--blue);display:flex;align-items:center;justify-content:center}
.call b{font-weight:400;color:var(--blue)}
/* hero */
.hero{height:468px;background:linear-gradient(180deg,#c9d5e6 0%,#9aa6bd 45%,#6f6f86 75%,#d9d4da 100%);position:relative}
.hero-caption{position:absolute;left:103px;top:299px;width:487px;height:116px;background:rgba(20,24,30,.72);border-left:5px solid var(--blue);padding:20px 26px;color:#fff}
.hero-caption h3{font-family:"Raleway",Arial,sans-serif;font-weight:600;font-size:19px;margin-bottom:10px}
.hero-caption p{font-size:11.5px;line-height:20px}
/* welcome */
.welcome{padding-top:55px}
.welcome .lead{font-size:16px;line-height:30px;margin-top:20px}
.rentals{display:flex;justify-content:space-between;margin-top:42px}
.rental{width:327px;text-align:center}
.photo{display:block;height:209px}
.rental h4{font-size:14.5px;font-weight:600;margin:22px 0 10px;color:#333}
.rental p,.service p,.post p{font-size:11.5px;line-height:24px;color:#666}
/* services */
.services{padding-top:84px}
.services .lead{margin-top:12px}
.service-grid{display:grid;grid-template-columns:350px 350px 302px;row-gap:56px;margin-top:56px}
.service{display:flex;gap:20px}
.service .ic{flex:none;width:67px;height:67px;border-radius:50%;display:flex;align-items:center;justify-content:center}
.service h4{font-size:13px;font-weight:600;color:#333;margin-top:-2px;margin-bottom:6px}
.service p{width:230px}
/* blog */
.blog{padding-top:74px}
.blog .lead{margin-top:12px}
.posts{display:flex;justify-content:space-between;margin-top:40px}
.post{width:234px}
.post .photo{height:163px}
.post h4{font-size:12px;font-weight:700;margin-top:16px;color:#333}
.post time{display:block;font-size:11px;color:#555;margin:4px 0 12px}
/* testimonials */
.testimonials{position:absolute;top:2059px;left:0;width:1200px;height:397px;background:var(--band);color:#fff}
.testimonials h2{color:#fff;padding-top:52px}
.testimonials .lead{color:#fff;margin-top:14px}
.quotes{display:flex;justify-content:space-between;margin-top:42px}
.quote{width:300px;position:relative;padding:0 20px 0 20px}
.quote::before{content:"\201C";position:absolute;left:-2px;top:-12px;font-size:34px;font-family:Georgia,serif}
.quote::after{content:"\201D";position:absolute;right:-2px;top:52px;font-size:34px;font-family:Georgia,serif}
.quote p{font-size:12px;line-height:24px}
.person{display:flex;align-items:center;gap:14px;margin-top:20px;margin-left:-20px}
.avatar{width:52px;height:52px;border-radius:50%;border:3px solid #d9e6f4;background:#b9a89a}
.person b{display:block;font-size:11px;font-weight:700}
.person span{font-size:10.5px}
/* footer */
.site-footer{position:absolute;top:2456px;left:0;width:1200px;height:304px;background:var(--dark);color:#ccc}
.site-footer h5{font-size:16px;font-weight:700;color:#fff;position:absolute}
.site-footer p,.site-footer li{font-size:11px;line-height:25px}
.find{position:absolute;left:101px;top:58px}
.find ul{list-style:none;margin-top:36px}
.find li svg{vertical-align:-2px;margin-right:8px}
.foot-brand{display:flex;align-items:center;gap:8px;margin-top:22px;font-family:"Raleway",Arial,sans-serif;font-weight:700;font-size:22px;color:#7fa9d6}
.foot-brand .dot{width:12px;height:12px;border-radius:50%;background:#7fa9d6}
.contact{position:absolute;left:393px;top:58px;width:386px}
.field{position:absolute;background:var(--field);border:1px solid #3a3a3a;font-size:10.5px;color:#bbb;padding:8px 10px}
.submit{position:absolute;left:200px;top:178px;width:186px;height:32px;background:#5b9de0;color:#fff;font-size:11px;font-weight:700;display:flex;align-items:center;justify-content:center;border-radius:2px}
.about{position:absolute;left:848px;top:58px;width:260px}
.about p{margin-top:36px;line-height:23px}
.follow{position:absolute;left:0;top:146px}
.socials{position:absolute;top:182px;left:0;display:flex;gap:8px}
.socials span{width:28px;height:28px;border-radius:50%;background:var(--blue)}
.bottom-bar{position:absolute;top:2760px;left:0;width:1200px;height:48px;background:var(--darker);color:#aaa;font-size:10.5px;display:flex;align-items:center;justify-content:center}
</style>
</head>
<body>
<header class="site-header">
  <div class="brand"><span class="dot"></span>Brightmoor Crest</div>
  <nav class="nav">
    <a style="left:400px" href="#">About Us</a>
    <a style="left:513px" href="#">Service<span class="caret">&#9660;</span></a>
    <a style="left:614px" href="#">Properties<span class="caret">&#9660;</span></a>
    <a style="left:732px" href="#">Blog</a>
    <a style="left:818px" href="#">Contact Us</a>
  </nav>
  <div class="call"><span class="ic"><svg width="16" height="16" viewBox="0 0 24 24"><path fill="#fff" d="M6.6 10.8a15 15 0 0 0 6.6 6.6l2.2-2.2c.3-.3.7-.4 1-.2 1.1.4 2.3.6 3.6.6.6 0 1 .4 1 1V20c0 .6-.4 1-1 1A17 17 0 0 1 3 4c0-.6.4-1 1-1h3.5c.6 0 1 .4 1 1 0 1.3.2 2.5.6 3.6.1.3 0 .7-.2 1z"/></svg></span>Call us : <b>( 555 ) 014 2280</b></div>
</header>

<section class="hero" role="img" aria-label="Modern two-storey glass house lit at dusk">
  <div class="hero-caption">
    <h3>We also offer Real Estate Listing services</h3>
    <p>We focus on residential rental properties. However we are looking to expand into multi-family rentals, commercial rentals, and vacation rentals.</p>
  </div>
</section>

<main>
<section class="wrap welcome">
  <h2>Welcome to Brightmoor Crest properties</h2>
  <p class="lead">We focus on residential rental properties. However we are looking to expand into multi-family rentals,<br>commercial rentals, and vacation rentals.</p>
  <div class="rentals">
    <article class="rental"><span class="photo" role="img" aria-label="Multi-family building with glass facade" style="background:linear-gradient(180deg,#b8cde0,#8c9aa6 60%,#5d7a4e)"></span><h4>Multi-family rentals</h4><p>Lorem Ipsum is simply dummy text of the printing and typesetting industry. Lorem Ipsum has been the industry's standard dummy....</p></article>
    <article class="rental"><span class="photo" role="img" aria-label="Commercial apartment tower against blue sky" style="background:linear-gradient(180deg,#3f78c4,#7fa4d6 55%,#c9c3bd)"></span><h4>Commercial rentals</h4><p>Lorem Ipsum is simply dummy text of the printing and typesetting industry. Lorem Ipsum has been the industry's standard dummy....</p></article>
    <article class="rental"><span class="photo" role="img" aria-label="Modern vacation house on a lawn" style="background:linear-gradient(180deg,#6f9fd8,#b9c7d4 45%,#5f8b3c 75%,#4c7a2e)"></span><h4>Vacation rentals</h4><p>Lorem Ipsum is simply dummy text of the printing and typesetting industry. Lorem Ipsum has been the industry's standard dummy....</p></article>
  </div>
</section>

<section class="wrap services">
  <h2>Real Estate Listing services</h2>
  <p class="lead">Lorem Ipsum is simply dummy text of the printing and typesetting industry has been the industry's standard</p>
  <div class="service-grid">
    <div class="service"><span class="ic" style="background:var(--c-blue)"><svg width="32" height="32" viewBox="0 0 32 32" fill="none" stroke="#fff" stroke-width="2"><path d="M4 16 16 5l12 11M8 13v14h16V13"/></svg></span><div><h4>Finance Real Estate</h4><p>Lorem Ipsum is simply dummy text of the printing and typesetting industry. Lorem Ipsum has been the industry...</p></div></div>
    <div class="service"><span class="ic" style="background:var(--c-red)"><svg width="32" height="32" viewBox="0 0 32 32" fill="none" stroke="#fff" stroke-width="2"><path d="M8 6h16v16H8zM4 26h24"/><path d="M19 10h-4a2 2 0 0 0 0 4h2a2 2 0 0 1 0 4h-4M16 8v12"/></svg></span><div><h4>Invest in Real Estate</h4><p>Lorem Ipsum is simply dummy text of the printing and typesetting industry. Lorem Ipsum has been the industry...</p></div></div>
    <div class="service"><span class="ic" style="background:var(--c-gold)"><svg width="32" height="32" viewBox="0 0 32 32" fill="none" stroke="#fff" stroke-width="2"><path d="M3 14l7-5 6 4 6-4 7 5M8 17l6 6 4-2 6-6"/></svg></span><div><h4>Lease Space</h4><p>Lorem Ipsum is simply dummy text of the printing and typesetting industry. Lorem Ipsum has been the industry...</p></div></div>
    <div class="service"><span class="ic" style="background:var(--c-teal)"><svg width="32" height="32" viewBox="0 0 32 32" fill="none" stroke="#fff" stroke-width="2"><rect x="8" y="4" width="16" height="24"/><path d="M11 8h10v5H11zM11 17h2M15 17h2M19 17h2M11 21h2M15 21h2M19 21h2"/></svg></span><div><h4>Manage Property Taxes</h4><p>Lorem Ipsum is simply dummy text of the printing and typesetting industry. Lorem Ipsum has been the industry...</p></div></div>
    <div class="service"><span class="ic" style="background:var(--c-pink)"><svg width="32" height="32" viewBox="0 0 32 32" fill="none" stroke="#fff" stroke-width="2"><path d="M6 28V12h7v16M13 28V5h8v23M21 28V14h6v14M4 28h25"/></svg></span><div><h4>Manage Property or Projects</h4><p>Lorem Ipsum is simply dummy text of the printing and typesetting industry. Lorem Ipsum has been the industry...</p></div></div>
    <div class="service"><span class="ic" style="background:var(--c-purple)"><svg width="32" height="32" viewBox="0 0 32 32" fill="none" stroke="#fff" stroke-width="2"><path d="M4 15 14 6l10 9M7 13v13h10"/><circle cx="22" cy="20" r="5"/><path d="m26 24 3 3"/></svg></span><div><h4>Recover Asset Value</h4><p>Lorem Ipsum is simply dummy text of the printing and typesetting industry. Lorem Ipsum has been the industry...</p></div></div>
  </div>
</section>

<section class="wrap blog">
  <h2>Recent Blog</h2>
  <p class="lead">Lorem Ipsum is simply dummy text of the printing and typesetting industry has been the industry's standard</p>
  <div class="posts">
    <article class="post"><span class="photo" role="img" aria-label="Hand holding house keys in front of a home" style="background:linear-gradient(135deg,#c9a77a,#e8e4dc 55%,#6f9fd0)"></span><h4>Lorem Ipsum is simply dummy</h4><time>Posted on 27 March 2016</time><p>Lorem Ipsum is simply dummy text of the printing and typesetting industry. Lorem Ipsum has been the industry...</p></article>
    <article class="post"><span class="photo" role="img" aria-label="Businessman holding a small house model" style="background:linear-gradient(135deg,#2b2b2b,#7a7a7a 55%,#c9c9c9)"></span><h4>Lorem Ipsum is simply dummy</h4><time>Posted on 27 March 2016</time><p>Lorem Ipsum is simply dummy text of the printing and typesetting industry. Lorem Ipsum has been the industry...</p></article>
    <article class="post"><span class="photo" role="img" aria-label="Man on a sofa beneath a sketched house outline" style="background:linear-gradient(180deg,#d8d6d2,#b9bcc2 60%,#8e939c)"></span><h4>Lorem Ipsum is simply dummy</h4><time>Posted on 27 March 2016</time><p>Lorem Ipsum is simply dummy text of the printing and typesetting industry. Lorem Ipsum has been the industry...</p></article>
    <article class="post"><span class="photo" role="img" aria-label="Open hands holding a glowing house icon" style="background:linear-gradient(180deg,#1d2a44,#33466a 60%,#1a2438)"></span><h4>Lorem Ipsum is simply dummy</h4><time>Posted on 27 March 2016</time><p>Lorem Ipsum is simply dummy text of the printing and typesetting industry. Lorem Ipsum has been the industry...</p></article>
  </div>
</section>
</main>

<section class="testimonials">
  <h2>What our client's say</h2>
  <p class="lead">Lorem Ipsum is simply dummy text of the printing and typesetting industry has been the industry's standard</p>
  <div class="wrap quotes">
    <figure class="quote"><p>Lorem Ipsum is simply dummy text of the printing and typesetting industry. Lorem Ipsum has been the industry's standard dummy text ever since...</p><figcaption class="person"><span class="avatar" role="img" aria-label="Client portrait"></span><div><b>MARCUS HALE</b><span>Business man</span></div></figcaption></figure>
    <figure class="quote"><p>Lorem Ipsum is simply dummy text of the printing and typesetting industry. Lorem Ipsum has been the industry's standard dummy text ever since...</p><figcaption class="person"><span class="avatar" role="img" aria-label="Client portrait"></span><div><b>MARCUS HALE</b><span>Business man</span></div></figcaption></figure>
    <figure class="quote"><p>Lorem Ipsum is simply dummy text of the printing and typesetting industry. Lorem Ipsum has been the industry's standard dummy text ever since...</p><figcaption class="person"><span class="avatar" role="img" aria-label="Client portrait" style="background:#d6b48f"></span><div><b>MARCUS HALE</b><span>Business man</span></div></figcaption></figure>
  </div>
</section>

<footer class="site-footer">
  <div class="find">
    <h5>FIND PROPERTIES</h5>
    <ul>
      <li>120 Street name, City name,<br>Country name : 652365</li>
      <li><svg width="11" height="11" viewBox="0 0 24 24"><path fill="#5b9de0" d="M6.6 10.8a15 15 0 0 0 6.6 6.6l2.2-2.2c.3-.3.7-.4 1-.2 1.1.4 2.3.6 3.6.6.6 0 1 .4 1 1V20c0 .6-.4 1-1 1A17 17 0 0 1 3 4c0-.6.4-1 1-1h3.5c.6 0 1 .4 1 1 0 1.3.2 2.5.6 3.6.1.3 0 .7-.2 1z"/></svg>Phone : ( 555 ) 014 2280</li>
      <li><svg width="11" height="11" viewBox="0 0 24 24"><path fill="#5b9de0" d="M2 5h20v14H2zm2 2v.5l8 5 8-5V7z"/></svg>Email : info@brightmoorcrest.com</li>
    </ul>
    <div class="foot-brand"><span class="dot"></span>Brightmoor Crest</div>
  </div>
  <div class="contact">
    <h5>CONTACT</h5>
    <span class="field" style="left:0;top:28px;width:189px;height:30px">Name</span>
    <span class="field" style="left:0;top:73px;width:189px;height:30px">Email</span>
    <span class="field" style="left:0;top:120px;width:189px;height:30px">Phone</span>
    <span class="field" style="left:200px;top:28px;width:186px;height:77px">Comments</span>
    <span class="submit" style="top:120px">SUBMIT NOW!</span>
  </div>
  <div class="about">
    <h5>ABOUT US</h5>
    <p>Lorem Ipsum is simply dummy text of the printing and typesetting industry. Lorem Ipsum has been the industry's standard dummy text ever since the 1500s.</p>
    <h5 class="follow">FOLLOW US</h5>
    <div class="socials"><span></span><span></span><span></span><span></span><span></span></div>
  </div>
</footer>
<div class="bottom-bar">&copy; 2016. Brightmoor Crest properties. All rights reserved.</div>
</body>
</html>
```